Real Estate Investment Company Needs A Business Card Designed

I need a business card designed for my use. We are a real estate investment company based in Omaha, Nebraska that specializes in buying, rehabbing and selling single family and multifamily properties. Would love designs that incorporate our logo and colors

Industry/Entity Type

Business

Contact Information for Business Card

Marlow Pettigrew | President & CEO
4837 North 52nd Avenue, Ste 200
Omaha, NE 68214
(402) 555-7428
marlow@quillfenhomes.example
www.QuillfenHomes.example

Font styles to use
Serif

Colors
0255a3
3276b5

Requirements
Must have
• Our logo

```html
<!DOCTYPE html>
<html lang="en">
<head>
<meta charset="utf-8">
<title>Quillfen Business Card</title>
<link rel="stylesheet" href="https://fonts.googleapis.com/css2?family=Work+Sans:wght@400;600;700&display=swap">
<style>
  :root {
    --stage: #232323;
    --card-dark: #1a1b1c;
    --brand-deep: #0255a3;
    --brand-mid: #3276b5;
    --brand-light: #64a8de;
    --silver: #c4c4c4;
    --white: #ffffff;
  }
  * { box-sizing: border-box; margin: 0; padding: 0; }
  html, body {
    width: 1200px; height: 852px; overflow: hidden;
    background: var(--stage);
    font-family: "Work Sans", Arial, sans-serif;
  }
  .stage {
    width: 1200px; height: 852px;
    display: flex; flex-direction: column;
    align-items: center; justify-content: center; gap: 40px;
  }
  .card {
    position: relative; width: 620px; height: 354px;
    border-radius: 18px; overflow: hidden;
    box-shadow: 0 10px 30px rgba(0,0,0,.45);
  }
  /* Front side */
  .card-front {
    background: var(--card-dark);
    display: flex; align-items: center; justify-content: center; gap: 14px;
  }
  .front-dot {
    width: 34px; height: 34px; border-radius: 50%;
    background: var(--brand-mid);
  }
  .front-name {
    font-weight: 700; font-size: 40px; letter-spacing: 1px;
    color: var(--brand-mid);
  }
  /* Back side */
  .card-back {
    background: linear-gradient(45deg, var(--brand-light) 0%, var(--brand-mid) 55%, var(--brand-deep) 100%);
    color: var(--white);
  }
  .back-panel { position: absolute; inset: 0; }
  .back-content { position: absolute; left: 34px; top: 58px; }
  .back-wordmark {
    font-weight: 700; font-size: 46px; letter-spacing: 1px; line-height: 1;
  }
  .person-name { margin-top: 46px; font-weight: 600; font-size: 23px; line-height: 1.1; }
  .person-title { font-weight: 400; font-size: 14px; margin-top: 2px; }
  .address { margin-top: 14px; font-size: 14px; line-height: 1.3; }
  .contacts { margin-top: 12px; list-style: none; font-size: 14px; line-height: 1.4; }
  .contacts li { display: flex; align-items: center; gap: 8px; }
  .contacts svg { width: 11px; height: 11px; fill: none; stroke: var(--white); stroke-width: 1.6; }
</style>
</head>
<body>
<main class="stage">
  <section class="card card-front" aria-label="Card front">
    <span class="front-dot"></span>
    <span class="front-name">QUILLFEN</span>
  </section>

  <section class="card card-back" aria-label="Card back">
    <svg class="back-panel" viewBox="0 0 620 354" aria-hidden="true">
      <polygon points="430,0 620,0 620,354 540,354" fill="var(--white)"/>
      <circle cx="486" cy="150" r="132" fill="var(--white)" stroke="var(--brand-mid)" stroke-width="8"/>
      <circle cx="486" cy="150" r="118" fill="none" stroke="var(--silver)" stroke-width="3"/>
    </svg>
    <div class="back-content">
      <div class="back-wordmark">QUILLFEN</div>
      <div class="person-name">Marlow Pettigrew</div>
      <div class="person-title">President &amp; CEO</div>
      <div class="address">4837 North 52nd Avenue, Ste 200<br>Omaha, NE 68214</div>
      <ul class="contacts">
        <li><svg viewBox="0 0 12 12"><path d="M2 1.5l2 0 1 2.5-1.2 1a6 6 0 0 0 3.2 3.2l1-1.2 2.5 1v2a1 1 0 0 1-1 1A9 9 0 0 1 1 2.5a1 1 0 0 1 1-1z"/></svg>(402) 555-7428</li>
        <li><svg viewBox="0 0 12 12"><rect x="1" y="2.5" width="10" height="7"/><path d="M1 2.5l5 4 5-4"/></svg>marlow@quillfenhomes.example</li>
        <li><svg viewBox="0 0 12 12"><circle cx="6" cy="6" r="5"/><path d="M1 6h10M6 1c-2.5 3-2.5 7 0 10M6 1c2.5 3 2.5 7 0 10"/></svg>www.QuillfenHomes.example</li>
      </ul>
    </div>
  </section>
</main>
</body>
</html>
```